Data Compass Plan- Brennal Insurance providing specialist Cyber and Liability Insurance

for Managed Technology Service Providers and their customer, we will use a letterhead that white labels insurer documents, which can be used in our physical letters as well as to be used within Email signatures.

Target Market(s)

Managed Technology Services Providers

Industry/Entity Type

Cyber Insurance

Requirements
Must have
• website, email address, contact phone numbers

```html
<!DOCTYPE html>
<html lang="en">
<head>
<meta charset="utf-8">
<title>Data Compass Plan – Letterhead</title>
<link rel="stylesheet" href="https://fonts.googleapis.com/css2?family=Lato:wght@400;700&family=Great+Vibes&display=swap">
<style>
  :root {
    --brand-green: #45b25b;
    --brand-green-deep: #3fa84f;
    --ink: #3d3d3d;
    --ink-soft: #4a4a4a;
    --stripe-gray: #4b4b4d;
    --paper: #f3f3f3;
    --backdrop: #dcdcdc;
  }
  * { box-sizing: border-box; margin: 0; padding: 0; }
  html, body {
    width: 1200px; height: 884px; overflow: hidden;
    background: var(--backdrop);
    font-family: "Lato", sans-serif;
    color: var(--ink);
  }
  .letterhead {
    position: absolute; left: 303px; top: 22px;
    width: 594px; height: 840px;
    background: var(--paper);
    box-shadow: 0 6px 18px rgba(0,0,0,.18);
    overflow: hidden;
  }
  .header-bands, .footer-bands { position: absolute; left: 0; width: 594px; }
  .header-bands { top: 0; height: 70px; }
  .footer-bands { bottom: 0; height: 70px; }

  .brand {
    position: absolute; left: 56px; top: 46px;
    display: flex; align-items: center; gap: 10px;
  }
  .brand-mark { width: 12px; height: 12px; background: var(--brand-green); }
  .brand-name {
    font-weight: 700; font-size: 26px; letter-spacing: 3px;
    text-transform: uppercase; color: var(--ink);
  }

  .contact {
    position: absolute; left: 392px; top: 104px;
    border-left: 1.5px solid var(--brand-green);
    padding-left: 10px;
    font-size: 10.5px; line-height: 1.5; color: var(--ink);
  }
  .contact-row { display: flex; align-items: center; gap: 5px; }
  .contact-row svg { width: 9px; height: 9px; flex: none; }
  .contact-address { padding-left: 14px; }

  .letter { position: absolute; left: 56px; top: 110px; width: 480px; font-size: 11px; line-height: 1.5; }
  .letter-date { margin-bottom: 12px; }
  .recipient { margin-bottom: 12px; }
  .recipient p { margin: 0; }
  .recipient-company { margin-top: 12px; }
  .salutation { font-weight: 700; font-size: 12px; margin: 96px 0 6px; }
  .letter-body p { margin-bottom: 10px; color: var(--ink-soft); }
  .closing { margin-top: 18px; }
  .signature {
    font-family: "Great Vibes", cursive;
    font-size: 34px; color: var(--ink); margin-top: 10px;
  }
</style>
</head>
<body>
<main class="letterhead">
  <svg class="header-bands" viewBox="0 0 594 70" aria-hidden="true">
    <polygon points="0,0 594,0 594,44 360,44 336,14 0,14" fill="var(--brand-green)"/>
    <polygon points="346,20 450,20 450,25 350,25" fill="var(--stripe-gray)" transform="translate(8,30)"/>
    <rect x="458" y="50" width="80" height="5" fill="var(--brand-green-deep)"/>
    <rect x="538" y="50" width="56" height="5" fill="var(--stripe-gray)"/>
  </svg>

  <div class="brand">
    <span class="brand-mark"></span>
    <span class="brand-name">Data Compass Plan</span>
  </div>

  <address class="contact">
    <div class="contact-address">42-10 Linden Ave 8,<br>Ridgefield, NY 11290</div>
    <div class="contact-row">
      <svg viewBox="0 0 10 10"><path d="M2 1h2l1 2.5-1.3 1a5 5 0 0 0 2 2l1-1.3L9 6v2a1 1 0 0 1-1 1A7 7 0 0 1 1 2a1 1 0 0 1 1-1z" fill="var(--brand-green)"/></svg>
      555-014-2267
    </div>
    <div class="contact-row">
      <svg viewBox="0 0 10 10"><rect x="0.5" y="2" width="9" height="6.5" fill="var(--brand-green)"/><path d="M0.8 2.4 5 5.6 9.2 2.4" stroke="#fff" stroke-width="0.9" fill="none"/></svg>
      info@datacompassplan.com
    </div>
    <div class="contact-row">
      <svg viewBox="0 0 10 10"><circle cx="5" cy="5" r="4.5" fill="var(--brand-green)"/><path d="M0.8 5h8.4M5 0.6c-2.4 2.6-2.4 6.2 0 8.8M5 0.6c2.4 2.6 2.4 6.2 0 8.8" stroke="#fff" stroke-width="0.7" fill="none"/></svg>
      www.datacompassplan.com
    </div>
  </address>

  <article class="letter">
    <p class="letter-date">Feb-03-2022</p>
    <div class="recipient">
      <p>Mr, Alan Reyes</p>
      <p>President</p>
      <p class="recipient-company">Northgate Systems</p>
      <p>123 Street Name, Suite# 10</p>
      <p>City, State, 120023</p>
    </div>
    <p class="salutation" style="margin-top:14px">Dear Mr, Alan</p>
    <div class="letter-body">
      <p>Lorem ipsum dolor sit amet, consectetur adipisicing elit, sed do eiusmod tempor incididunt ut labore et dolore magna aliqua. Ut enim ad minim veniam, quis nostrud exercitation ullamco laboris nisi ut aliquip ex ea commodo consequat. Duis aute irure dolor in reprehenderit in voluptate velit esse cillum dolore eu fugiat nulla pariatur.</p>
      <p>Lorem ipsum dolor sit amet, consectetur adipisicing elit, sed do eiusmod tempor incididunt ut labore et dolore magna aliqua. Ut enim ad minim veniam, quis nostrud exercitation ullamco laboris nisi ut aliquip ex ea commodo consequat. Duis aute irure dolor in reprehenderit in voluptate velit esse cillum dolore eu fugiat nulla pariatur.</p>
      <p>Lorem ipsum dolor sit amet, consectetur adipisicing elit, sed do eiusmod tempor incididunt ut labore et dolore magna aliqua. Ut enim ad minim veniam, quis nostrud exercitation ullamco laboris nisi ut aliquip ex ea commodo consequat.<br>Excepteur sint occaecat cupidatat non proident, sunt in culpa qui officia deserunt mollit anim id est laborum. re et dolore magnam aliquam quaerat voluptatem.</p>
    </div>
    <p class="closing">Regards</p>
    <p class="signature">Daniel Hart</p>
  </article>

  <svg class="footer-bands" viewBox="0 0 594 70" aria-hidden="true">
    <rect x="0" y="15" width="70" height="5" fill="var(--stripe-gray)"/>
    <rect x="70" y="15" width="82" height="5" fill="var(--brand-green-deep)"/>
    <rect x="152" y="15" width="92" height="5" fill="var(--stripe-gray)"/>
    <polygon points="0,26 250,26 274,56 594,56 594,70 0,70" fill="var(--brand-green)"/>
  </svg>
</main>
</body>
</html>
```